PSD website for property company

Please read the brief thoroughly.

We are looking for a new website for a property group that does property acquisitions, property development and property management.
They buy, build and lease core inner city industrial assets in Sydney, Australia.
They also invest in residential developments.

Site menu
- Home page
- Property – sub menus include – Leasing ; Projects ; Investments ; Property Management
- Capital and finance
- About
- Contact

They like this website
https://www.verlo.com.au/

They want the site to be clean, modern and bold.
They like few colors, even black and white is OK to submit

They have a logo and style guide and useable images here:
http://www.kumet.net/temp/PelorisWeb2019.zip
The zip file is also attached to this project.
We have supplied some images to give you an idea, but we will also require you to provide at least 3 extra images from stock photos.
Use your imagination.

I am expecting a lot of similar designs, so be aware the photos you choose will be really important.
They want really 3 good stock photos used and supplied without charge.
Please not too generic, I repeat the quality of the photos is important.
You may provide several photos (but not in multiple submissions please) and we will choose the best three to be provided.

The winner will be selected on a single home page design and required to provide;
All photos use in original format without charge
A second ‘standard page’ template design based on the winning home page design

```html
<!DOCTYPE html>
<html lang="en">
<head>
<meta charset="utf-8">
<title>Peloris – Your Property Solution</title>
<link rel="stylesheet" href="https://fonts.googleapis.com/css2?family=Arimo:wght@400;700&family=Montserrat:wght@700&display=swap">
<style>
  :root{
    --green:#4b6b2a;
    --green-bright:#557a2e;
    --dark:#2b2b2b;
    --ink:#222;
    --grey:#777;
    --line:#d6d6d6;
    --white:#fff;
  }
  *{box-sizing:border-box;margin:0;padding:0}
  html,body{width:1200px;height:4193px;overflow:hidden}
  body{position:relative;background:var(--white);font-family:'Arimo',Arial,sans-serif;color:var(--ink)}
  .abs{position:absolute}
  .site-header{position:absolute;left:0;top:0;width:1200px;height:78px;background:var(--white)}
  .brand{position:absolute;font-family:'Montserrat',Arial,sans-serif;font-weight:700;letter-spacing:6px}
  .brand--header{left:84px;top:24px;font-size:30px;color:var(--dark)}
  .call{position:absolute;left:912px;top:18px;display:flex;gap:10px;align-items:center}
  .call__label{font-size:13px;font-weight:700;color:var(--green);line-height:16px}
  .call__num{font-size:13px;color:var(--grey);line-height:16px}
  .main-nav{position:absolute;left:0;top:78px;width:1200px;height:57px;background:var(--dark)}
  .main-nav a{position:absolute;top:0;height:57px;line-height:57px;color:var(--white);font-size:14px;text-decoration:none;transform:translateX(-50%)}
  .main-nav a.is-active{left:161px;width:124px;transform:none;text-align:center;background:var(--green)}
  .hero{position:absolute;left:0;top:135px;width:1200px;height:710px}
  .hero__title{position:absolute;left:0;top:240px;width:1200px;text-align:center;color:var(--white);font-size:50px;font-weight:700;letter-spacing:.5px;text-shadow:0 2px 6px rgba(0,0,0,.25)}
  .btn{position:absolute;display:flex;align-items:center;justify-content:center;gap:12px;font-size:14px;text-decoration:none;text-transform:uppercase}
  .btn--light{background:var(--white);color:var(--ink)}
  .btn--dark{background:var(--dark);color:var(--white)}
  .section-title{position:absolute;left:0;width:1200px;text-align:center;color:var(--green);font-weight:700;font-size:33px;line-height:40px}
  .lead{position:absolute;left:0;width:1200px;text-align:center;color:var(--grey);font-size:14px}
  .card{position:absolute;top:1060px;width:331px;text-align:center}
  .card--raised{height:457px;background:var(--white);box-shadow:0 4px 14px rgba(0,0,0,.16)}
  .card__photo{width:331px;height:207px}
  .card__icon{position:absolute;left:119px;top:162px;width:93px;height:93px;border-radius:50%;background:var(--white);display:flex;align-items:center;justify-content:center}
  .card__title{position:absolute;left:0;top:257px;width:100%;font-size:20px;font-weight:700;color:var(--ink)}
  .card__text{position:absolute;left:10px;top:290px;width:311px;font-size:14px;line-height:24px;color:var(--grey)}
  .card__go{position:absolute;left:149px;top:402px}
  .split-title{position:absolute;color:var(--green);font-weight:700;font-size:33px}
  .body-copy{position:absolute;font-size:14px;line-height:24px;color:var(--grey)}
  .photo{position:absolute}
  .field{position:absolute;left:330px;width:547px;border:1px solid var(--line);background:rgba(255,255,255,.85);font-size:13px;color:#aaa;padding:0 24px}
  .site-footer{position:absolute;left:0;top:4041px;width:1200px;height:152px;background:var(--dark)}
  .brand--footer{left:130px;top:30px;font-size:36px;color:var(--green)}
  .foot-link{position:absolute;top:42px;font-size:14px;color:var(--white)}
  .social{position:absolute;top:46px;width:14px;height:14px;border-radius:50%;background:var(--white)}
  .copyright{position:absolute;left:0;top:98px;width:1200px;text-align:center;font-size:14px;color:var(--white)}
</style>
</head>
<body>

<header class="site-header">
  <div class="brand brand--header">PELORIS</div>
  <div class="call">
    <svg width="34" height="34" viewBox="0 0 34 34" aria-hidden="true"><circle cx="17" cy="17" r="15" fill="none" stroke="var(--green)" stroke-width="2.5"/><path d="M11 10c1-1 2-1 3 0l2 3c.5 1 0 2-1 2.5 1 2 2.5 3.5 4.5 4.5.5-1 1.5-1.5 2.5-1l3 2c1 1 1 2 0 3-2 2-5 1.5-8-1s-6-5.5-7.5-8.5-1-3.5 1.5-4.5z" fill="var(--green)"/></svg>
    <div><div class="call__label">CALL US NOW</div><div class="call__num">+00 123 456 789</div></div>
  </div>
</header>

<nav class="main-nav">
  <a class="is-active" href="#">Home</a>
  <a href="#" style="left:391px">Property</a>
  <a href="#" style="left:604px">Capital and finance</a>
  <a href="#" style="left:804px">About</a>
  <a href="#" style="left:972px">Contact</a>
</nav>

<section class="hero">
  <svg class="abs" style="left:0;top:0" width="1200" height="710" viewBox="0 0 1200 710">
    <defs>
      <linearGradient id="heroSky" x1="0" y1="0" x2="0" y2="1">
        <stop offset="0" stop-color="#8fa6b6"/><stop offset=".45" stop-color="#b9b4aa"/><stop offset=".75" stop-color="#7a7a5e"/><stop offset="1" stop-color="#5f6646"/>
      </linearGradient>
    </defs>
    <path d="M0 0H1200V560Q600 820 0 560Z" fill="var(--green)"/>
    <path d="M0 0H1200V556Q600 800 0 556Z" fill="url(#heroSky)" role="img" aria-label="Photo of a modern mixed-use building with arched ground floor and landscaped courtyard"/>
    <rect x="591" y="617" width="16" height="26" rx="8" fill="none" stroke="#fff" stroke-width="2"/>
    <line x1="599" y1="623" x2="599" y2="630" stroke="#fff" stroke-width="2"/>
  </svg>
  <h1 class="hero__title">YOUR PROPERTY SOLUTION</h1>
  <a class="btn btn--light" href="#" style="left:473px;top:321px;width:253px;height:49px">Explore our projects
    <svg width="16" height="12" viewBox="0 0 16 12"><path d="M2 1l5 5-5 5M8 1l5 5-5 5" fill="none" stroke="currentColor" stroke-width="2"/></svg></a>
</section>

<h2 class="section-title" style="top:887px">PELORIS – Family owned and operated,<br>community orientated</h2>
<p class="lead" style="top:996px">Putting 45 years of local experience to work for the Inner West</p>

<article class="card" style="left:80px">
  <div class="card__photo" role="img" aria-label="Photo of a lease agreement with keys" style="background:linear-gradient(135deg,#3b56a8,#dfe4f0 55%,#e9a07a)"></div>
  <div class="card__icon"><svg width="40" height="40" viewBox="0 0 40 40"><rect x="5" y="4" width="24" height="30" rx="2" fill="none" stroke="var(--green)" stroke-width="3"/><path d="M10 12h14M10 18h10M10 24h7" stroke="var(--green)" stroke-width="2.5"/><path d="M33 14l4 4-13 13-6 2 2-6z" fill="var(--green)"/></svg></div>
  <h3 class="card__title">Leasing</h3>
  <p class="card__text">Lorem Ipsum is simply dummy text of the printing and typesetting industry. Lorem Ipsum has been the industry's standard dummy text ever since the 1500s.</p>
  <svg class="card__go" width="33" height="33" viewBox="0 0 33 33"><circle cx="16.5" cy="16.5" r="15.5" fill="none" stroke="#333" stroke-width="1.5"/><path d="M14 11l5 5.5-5 5.5" fill="none" stroke="#333" stroke-width="1.5"/></svg>
</article>

<article class="card card--raised" style="left:435px">
  <div class="card__photo" role="img" aria-label="Photo of a small house model on stacks of coins with seedlings" style="background:linear-gradient(180deg,#3e4550,#5a5f62 60%,#33373a)"></div>
  <div class="card__icon"><svg width="40" height="40" viewBox="0 0 40 40"><path d="M4 36h32" stroke="var(--green)" stroke-width="3"/><rect x="8" y="24" width="6" height="10" fill="var(--green)"/><rect x="17" y="18" width="6" height="16" fill="var(--green)"/><rect x="26" y="12" width="6" height="22" fill="var(--green)"/><path d="M6 18L18 8l6 5 10-9" fill="none" stroke="var(--green)" stroke-width="2.5"/></svg></div>
  <h3 class="card__title">Investment</h3>
  <p class="card__text">Lorem Ipsum is simply dummy text of the printing and typesetting industry. Lorem Ipsum has been the industry's standard dummy text ever since the 1500s.</p>
  <svg class="card__go" width="33" height="33" viewBox="0 0 33 33"><circle cx="16.5" cy="16.5" r="16" fill="var(--green)"/><path d="M14 11l5 5.5-5 5.5" fill="none" stroke="#fff" stroke-width="1.8"/></svg>
</article>

<article class="card" style="left:788px">
  <div class="card__photo" role="img" aria-label="Photo of a couple receiving house keys from an agent" style="background:linear-gradient(90deg,#c9c2b4,#e7e4dd 50%,#8a8278)"></div>
  <div class="card__icon"><svg width="40" height="40" viewBox="0 0 40 40"><path d="M20 5L3 19h5v16h24V19h5z" fill="var(--green)"/><rect x="16" y="22" width="8" height="8" fill="#fff"/></svg></div>
  <h3 class="card__title">Property Managemnet</h3>
  <p class="card__text">Lorem Ipsum is simply dummy text of the printing and typesetting industry. Lorem Ipsum has been the industry's standard dummy text ever since the 1500s.</p>
  <svg class="card__go" width="33" height="33" viewBox="0 0 33 33"><circle cx="16.5" cy="16.5" r="15.5" fill="none" stroke="#333" stroke-width="1.5"/><path d="M14 11l5 5.5-5 5.5" fill="none" stroke="#333" stroke-width="1.5"/></svg>
</article>

<h2 class="split-title" style="left:81px;top:1683px">Capital and finance</h2>
<p class="body-copy" style="left:83px;top:1746px;width:405px">Lorem Ipsum is simply dummy text of the printing and typesetting industry. Lorem Ipsum has been the industry's standard dummy text ever since the 1500s, when an unknown printer took a galley of type and scrambled it to make a type specimen book. It has survived not only five centuries, but also the leap into electronic typesetting, remaining essentially unchanged.</p>
<a class="btn btn--dark" href="#" style="left:83px;top:1958px;width:176px;height:44px">Read more
  <svg width="16" height="12" viewBox="0 0 16 12"><path d="M2 1l5 5-5 5M8 1l5 5-5 5" fill="none" stroke="currentColor" stroke-width="2"/></svg></a>
<div class="photo" role="img" aria-label="Photo of a curved brick apartment building on a street corner" style="left:633px;top:1654px;width:487px;height:399px;background:linear-gradient(180deg,#9fb6cc,#6a4c3c 45%,#4a3a30 85%,#8a8a80)"></div>

<h2 class="section-title" style="top:2155px">Recently Projects</h2>
<div class="photo" role="img" aria-label="Photo of a large suburban family home" style="left:80px;top:2245px;width:337px;height:280px;background:linear-gradient(180deg,#2d6bd0,#b9b29c 55%,#5a8a36)"></div>
<div class="photo" role="img" aria-label="Photo of a modern residential tower with balconies" style="left:431px;top:2245px;width:337px;height:575px;background:linear-gradient(180deg,#2b7ed8,#c9d3dc 40%,#5f6c70 80%,#4e6e3a)"></div>
<div class="photo" role="img" aria-label="Photo of a white apartment block with glass balconies" style="left:783px;top:2245px;width:337px;height:280px;background:linear-gradient(180deg,#1f86de,#e8eef2 60%,#7a8a5a)"></div>
<div class="photo" role="img" aria-label="Photo of an industrial warehouse at sunset" style="left:80px;top:2540px;width:337px;height:280px;background:linear-gradient(180deg,#3b6fbf,#6d7ea6 55%,#4f5a78)"></div>
<div class="photo" role="img" aria-label="Photo of modern townhouses with red and white facades" style="left:783px;top:2540px;width:337px;height:280px;background:linear-gradient(180deg,#1e8ae0,#dfe2e4 55%,#5c6a3e)"></div>
<a class="btn btn--dark" href="#" style="left:477px;top:2877px;width:247px;height:44px">View more projects
  <svg width="16" height="12" viewBox="0 0 16 12"><path d="M2 1l5 5-5 5M8 1l5 5-5 5" fill="none" stroke="currentColor" stroke-width="2"/></svg></a>

<div class="photo" role="img" aria-label="Photo of a brick building with large arched windows" style="left:85px;top:3013px;width:486px;height:399px;background:linear-gradient(180deg,#a9c0d2,#ddd9d0 35%,#6e4b38 60%,#4b3a30)"></div>
<h2 class="split-title" style="left:667px;top:3055px">About us</h2>
<p class="body-copy" style="left:668px;top:3120px;width:405px">Lorem Ipsum is simply dummy text of the printing and typesetting industry. Lorem Ipsum has been the industry's standard dummy text ever since the 1500s, when an unknown printer took a galley of type and scrambled it to make a type specimen book. It has survived not only five centuries, but also the leap into electronic typesetting, remaining essentially unchanged.</p>
<a class="btn btn--dark" href="#" style="left:669px;top:3331px;width:176px;height:44px">Read more
  <svg width="16" height="12" viewBox="0 0 16 12"><path d="M2 1l5 5-5 5M8 1l5 5-5 5" fill="none" stroke="currentColor" stroke-width="2"/></svg></a>

<section class="abs" role="img" aria-label="Faded photo of a bright interior" style="left:0;top:3435px;width:1200px;height:606px;background:linear-gradient(180deg,#fff,#f1f1ef 40%,#e8e8e5)"></section>
<h2 class="section-title" style="top:3555px">Keep up to date</h2>
<div class="field" style="top:3626px;height:42px;line-height:40px">Full Name</div>
<div class="field" style="top:3683px;height:42px;line-height:40px">Phone#</div>
<div class="field" style="top:3740px;height:42px;line-height:40px">Email Address</div>
<div class="field" style="top:3798px;height:130px;padding-top:20px">Message</div>
<a class="btn btn--dark" href="#" style="left:511px;top:3945px;width:187px;height:42px;text-transform:none">SUBMIT NOW
  <svg width="16" height="12" viewBox="0 0 16 12"><path d="M2 1l5 5-5 5M8 1l5 5-5 5" fill="none" stroke="currentColor" stroke-width="2"/></svg></a>

<footer class="site-footer">
  <div class="brand brand--footer">PELORIS</div>
  <span class="foot-link" style="left:417px">Terms of Use &amp; Privacy Policy</span>
  <span class="abs" style="left:644px;top:38px;width:1px;height:24px;background:#fff"></span>
  <span class="foot-link" style="left:680px">Customer Care</span>
  <span class="social" style="left:846px;background:var(--green)"></span>
  <span class="social" style="left:889px"></span>
  <span class="social" style="left:929px"></span>
  <span class="social" style="left:969px"></span>
  <span class="social" style="left:1011px"></span>
  <span class="social" style="left:1052px"></span>
  <p class="copyright">Copyright © 2019 Peloris.All Right Rresreved</p>
</footer>

</body>
</html>
```